swimming pool chlorine

its label for new items we have its coming with different package 5 & 10 & 45 kg drums its specialized for making the swimming pool clean of all dirts we have our logo which I will attach its " Valmo" but we need the label to show the clear of pool and the logo in middle top and down write " TORVA 60 with nice design. under this name of metreal "TRICHOROISOCYANURIC ACID" and we want to add some advantage of the product which is" Strong bleaching and disinfection effects, Long-term effects, Killing Bacteria and Algae, Quality Guarantee.

```html
<!DOCTYPE html>
<html lang="en">
<head>
<meta charset="utf-8">
<title>Valmo TORVA 60 – Pool Chlorine Label</title>
<link href="https://fonts.googleapis.com/css2?family=Michroma&family=Oswald:wght@600&display=swap" rel="stylesheet">
<style>
  :root {
    --sky-pale: #eaf5fa;
    --sky-light: #c6e5f2;
    --band-cyan: #35b9e6;
    --band-deep: #1f7fbf;
    --navy: #1d3f8f;
    --logo-red: #d8262f;
    --white: #ffffff;
    --water-deep: #1a4f98;
    --water-mid: #4f8fc8;
  }
  html, body {
    margin: 0;
    padding: 0;
    width: 1200px;
    height: 1200px;
    overflow: hidden;
    background: var(--white);
  }
  .label {
    display: block;
    width: 1200px;
    height: 1200px;
  }
  .claim-arc {
    font-family: "Michroma", sans-serif;
    font-size: 34px;
    font-weight: 700;
    fill: var(--navy);
    letter-spacing: 2px;
  }
  .badge-text {
    font-family: "Oswald", sans-serif;
    font-weight: 600;
    fill: var(--white);
    text-anchor: middle;
  }
  .brand-name {
    font-family: "Michroma", sans-serif;
    font-size: 128px;
    fill: var(--logo-red);
    text-anchor: middle;
  }
  .product-name {
    font-family: "Michroma", sans-serif;
    font-size: 104px;
    fill: var(--white);
    stroke: var(--navy);
    stroke-width: 3px;
    paint-order: stroke;
    font-style: italic;
  }
  .chemical-name {
    font-family: "Michroma", sans-serif;
    font-size: 30px;
    fill: var(--navy);
  }
  .benefit {
    font-family: "Michroma", sans-serif;
    font-size: 28px;
    fill: var(--logo-red);
    font-style: italic;
  }
  .net-weight {
    font-family: "Michroma", sans-serif;
    font-size: 52px;
    fill: var(--navy);
  }
</style>
</head>
<body>
<svg class="label" viewBox="0 0 1200 1200" xmlns="http://www.w3.org/2000/svg">
  <defs>
    <radialGradient id="label-glow" cx="0.65" cy="0.3" r="0.9">
      <stop offset="0" stop-color="#ffffff"/>
      <stop offset="0.45" stop-color="#eaf5fa"/>
      <stop offset="1" stop-color="#c6e5f2"/>
    </radialGradient>
    <linearGradient id="band-top" x1="0" y1="0" x2="1" y2="0">
      <stop offset="0" stop-color="#1f7fbf"/>
      <stop offset="1" stop-color="#4aa6d8"/>
    </linearGradient>
    <linearGradient id="water-fill" x1="0" y1="0" x2="0" y2="1">
      <stop offset="0" stop-color="#4f8fc8" stop-opacity="0.7"/>
      <stop offset="1" stop-color="#1a4f98"/>
    </linearGradient>
    <path id="claim-curve" d="M250 560 C 360 420, 760 380, 880 450"/>
  </defs>

  <rect class="label-bg" width="1200" height="1200" fill="url(#label-glow)"/>

  <path class="swoosh-deep" d="M0 0 H1200 V30 C 820 70, 330 190, 0 470 Z" fill="url(#band-top)"/>
  <path class="swoosh-cyan" d="M0 470 C 330 190, 820 70, 1200 30 V80 C 830 110, 360 230, 0 540 Z" fill="var(--band-cyan)"/>

  <text class="claim-arc"><textPath href="#claim-curve" startOffset="2%">LONG-TERM EFFECTS</textPath></text>

  <g class="quality-badge">
    <circle cx="975" cy="470" r="92" fill="var(--band-deep)"/>
    <text class="badge-text" x="975" y="468" font-size="46">QUALITY</text>
    <text class="badge-text" x="975" y="510" font-size="30">GUARANTEE</text>
  </g>

  <text class="brand-name" x="590" y="680">Valmo</text>

  <g role="img" aria-label="Clear pool water splash wave">
    <path d="M0 1200 V1095 C 150 1045, 260 1075, 380 1105 C 540 1145, 640 1170, 780 1135 C 920 1095, 1020 1000, 1200 950 V1200 Z" fill="url(#water-fill)"/>
  </g>

  <g class="product-block" transform="rotate(-5 620 820)">
    <polygon class="product-plate" points="200,740 1040,740 1010,860 180,860" fill="var(--band-cyan)"/>
    <text class="product-name" x="215" y="845">TORVA 60</text>
    <rect class="product-rule" x="185" y="870" width="830" height="6" fill="var(--band-deep)"/>
    <text class="chemical-name" x="200" y="918">TRICHOROISOCYANURIC ACID</text>
    <text class="benefit" x="195" y="966">KILLING BACTERIA AND ALGAE</text>
  </g>

  <text class="net-weight" x="790" y="1010">10kg</text>
</svg>
</body>
</html>
```